Landing page for 'Page under construction' page

We need a simple landing page that we can use while our page is under construction.

The page should be made ready so that all we need to do is drop it on our web server and then it will function as our webpage. The domain is www.tlv.no

Please see attached file for instructions on what elements to include in the landing page. The Brand Book provides fonts and color palette.

Coding

Coded - Design and coding required

Number of Pages Required

1 page

Colors

Designer to choose colors to be used in the design.

```html
<!DOCTYPE html>
<html lang="en">
<head>
<meta charset="utf-8">
<title>Tallverk – Page is under construction</title>
<link rel="stylesheet" href="https://fonts.googleapis.com/css2?family=Nunito+Sans:wght@400;600;700;800&display=swap">
<style>
:root{
  --hero-deep:#143f6e;
  --hero-mid:#1d5e8e;
  --hero-light:#2f86a9;
  --navy:#1b3e73;
  --accent-red:#e8453c;
  --accent-orange:#f28c38;
  --ink:#1f2233;
  --body:#3a3d4a;
  --line-blue:#3d8fc9;
  --lavender:#e6e6fa;
  --soft-circle:#e8eef6;
  --white:#ffffff;
}
*{margin:0;padding:0;box-sizing:border-box}
html,body{width:1200px;height:2789px;overflow:hidden;background:var(--white)}
body{font-family:"Nunito Sans",Arial,sans-serif;color:var(--ink)}
.page{position:relative;width:1200px;height:2789px;overflow:hidden}
.decor{position:absolute;left:0;top:0;width:1200px;height:2789px}
.abs{position:absolute}

.brand{font-weight:800;color:var(--white);letter-spacing:.5px}
.hero-brand{left:206px;top:58px;font-size:40px}
.hero-mail{left:810px;top:68px;font-size:14px;font-weight:700;color:var(--white);display:flex;align-items:center;gap:12px}
.hero-title{left:206px;top:232px;font-size:29px;font-weight:700;color:var(--white)}
.countdown{left:206px;top:310px;display:flex;gap:13px}
.count-box{width:80px;height:86px;border:1px solid rgba(255,255,255,.22);background:rgba(16,52,100,.45);border-radius:4px;color:var(--white);text-align:center;padding-top:20px}
.count-box b{display:block;font-size:20px;font-weight:800}
.count-box span{font-size:14px}
.scroll-down{left:374px;top:438px;width:28px;height:28px}

.art{border-radius:6px}
.art-construction{left:630px;top:255px;width:505px;height:300px;border-radius:48% 52% 40% 60%/55% 50% 50% 45%;background:linear-gradient(135deg,#ecebfb,#d6d8f6 60%,#c4c9f2)}
.art-dashboard{left:208px;top:640px;width:337px;height:350px;background:linear-gradient(180deg,#dff1f1,#5b7fe6 45%,#3c64d8 70%,#ffffff)}
.art-bulb{left:597px;top:1201px;width:175px;height:227px;border-radius:48px 48px 58px 58px;background:radial-gradient(circle at 50% 40%,#4fc6f0,#0f5e9c 55%,#0a2c55)}
.art-server{left:801px;top:1240px;width:174px;height:280px;border-radius:40px 40px 70px 70px;background:radial-gradient(circle at 50% 45%,#3ab0e6,#14357a 55%,#08134a)}
.art-stacks{left:213px;top:1715px;width:323px;height:339px;background:linear-gradient(160deg,#c9c5ea,#4a5bc9 45%,#38e0c8 85%,#ffffff)}

.section-heading{font-size:24px;font-weight:800;line-height:1.3;color:var(--ink)}
.section-heading em{font-style:normal;font-weight:600;color:var(--accent-red)}
.intro-heading{left:615px;top:668px;width:390px}
.intro-bars{left:615px;top:774px;display:flex;gap:8px}
.intro-bars i{display:block;height:4px;border-radius:2px}
.text{font-size:10.5px;line-height:1.4;color:var(--body)}
.intro-text{left:615px;top:792px;width:375px}

.feature-title{font-size:24px;font-weight:600;color:var(--accent-red)}
.vision-icon{left:240px;top:1218px;width:32px;height:32px}
.vision-title{left:254px;top:1280px}
.vision-text{left:254px;top:1340px;width:285px}
.focus-icon{left:620px;top:1680px;width:36px;height:36px}
.focus-title{left:615px;top:1735px}
.focus-text{left:615px;top:1790px;width:345px}
.focus-text p{margin-bottom:11px}

.subscribe{left:237px;top:2205px;width:741px;height:285px;border-radius:14px;overflow:hidden;background:linear-gradient(180deg,#2c7fa3,#1d5e8e 50%,#173f74);color:var(--white);text-align:center}
.subscribe .wave{position:absolute;right:-30px;bottom:-20px;width:200px;height:180px;border-radius:50%;background:rgba(255,255,255,.06)}
.subscribe h2{margin-top:40px;font-size:28px;font-weight:700}
.subscribe .sub{font-size:13px;opacity:.9;margin-top:-2px}
.signup{display:flex;width:351px;height:44px;margin:28px auto 0;border-radius:3px;overflow:hidden}
.signup .field{flex:0 0 250px;background:#fdf4f2;color:#b4b4c0;font-size:11px;text-align:left;padding:15px 0 0 32px}
.signup .btn{flex:1;background:var(--accent-orange);color:var(--white);font-size:12px;font-weight:800;padding-top:15px}
.subscribe .contact{margin-top:34px;font-size:18px}
.subscribe .mail{margin-top:14px;font-size:16px;font-weight:700;display:flex;justify-content:center;align-items:center;gap:14px}

.footer-brand{left:0;width:1200px;top:2640px;text-align:center;font-size:40px}
.copyright{left:0;width:1200px;top:2728px;text-align:center;font-size:9px;color:rgba(255,255,255,.8)}
</style>
</head>
<body>
<main class="page">
  <svg class="decor" viewBox="0 0 1200 2789" aria-hidden="true">
    <defs>
      <linearGradient id="heroFill" x1="0" y1="0" x2="1" y2="1">
        <stop offset="0" stop-color="#1a5488"/>
        <stop offset=".55" stop-color="#23699a"/>
        <stop offset="1" stop-color="#3a90ad"/>
      </linearGradient>
      <linearGradient id="footFill" x1="0" y1="0" x2="0" y2="1">
        <stop offset="0" stop-color="#1f6893"/>
        <stop offset="1" stop-color="#173f74"/>
      </linearGradient>
    </defs>
    <path d="M0 0H1200V415C1100 405 960 430 820 470C680 515 610 545 520 545C310 545 110 470 0 360Z" fill="url(#heroFill)"/>
    <circle cx="118" cy="2318" r="125" fill="var(--soft-circle)"/>
    <path d="M0 2700C300 2600 600 2545 900 2570C1030 2580 1120 2595 1200 2610V2789H0Z" fill="url(#footFill)"/>
    <g fill="none" stroke="var(--line-blue)" stroke-width="2" stroke-dasharray="8 6">
      <path d="M742 922V1103H298V1186"/>
      <path d="M298 1414V1564H683V1635"/>
    </g>
    <g fill="none" stroke="var(--line-blue)" stroke-width="2">
      <circle cx="742" cy="915" r="6"/>
      <circle cx="298" cy="1407" r="6"/>
    </g>
  </svg>

  <div class="abs art" role="img" aria-label="Photograph of people reviewing business charts behind the header" style="left:0;top:0;width:0;height:0"></div>

  <div class="abs brand hero-brand">tallverk</div>
  <div class="abs hero-mail">
    <svg width="20" height="15" viewBox="0 0 20 15" aria-hidden="true"><rect x="1" y="1" width="18" height="13" fill="none" stroke="#fff" stroke-width="1.4"/><path d="M1 1l9 7 9-7M1 14l7-6M19 14l-7-6" fill="none" stroke="#fff" stroke-width="1.4"/></svg>
    media@tlv.no
  </div>
  <h1 class="abs hero-title">Page is under construction</h1>
  <div class="abs countdown">
    <div class="count-box"><b>90</b><span>Days</span></div>
    <div class="count-box"><b>10</b><span>Hours</span></div>
    <div class="count-box"><b>50</b><span>Minutes</span></div>
    <div class="count-box"><b>30</b><span>Seconds</span></div>
  </div>
  <svg class="abs scroll-down" viewBox="0 0 28 28" aria-hidden="true"><circle cx="14" cy="14" r="13" fill="none" stroke="rgba(255,255,255,.5)"/><path d="M14 7v13M9 15l5 5 5-5" fill="none" stroke="#fff" stroke-width="1.5"/></svg>
  <div class="abs art art-construction" role="img" aria-label="Illustration of workers at a construction site with a crane and warning sign"></div>

  <div class="abs art art-dashboard" role="img" aria-label="Illustration of two people analysing charts on a large screen"></div>
  <h2 class="abs section-heading intro-heading"><em>Digital solutions</em> and data-driven business development that create value.</h2>
  <div class="abs intro-bars">
    <i style="width:76px;background:var(--navy)"></i>
    <i style="width:30px;background:var(--accent-orange)"></i>
    <i style="width:30px;background:var(--accent-orange)"></i>
    <i style="width:30px;background:var(--accent-orange)"></i>
  </div>
  <p class="abs text intro-text">TLV Consulting is a consulting company with cutting-edge expertise in digitalisation and data-driven business development. We have extensive experience in data warehouse development, data analysis and reporting, EPM and planning solutions, budget and forecasting solutions for financial and financial data. In short, we help our customers exploit the potential in the available data.</p>

  <svg class="abs vision-icon" viewBox="0 0 32 32" aria-hidden="true"><circle cx="14" cy="14" r="10" fill="none" stroke="var(--navy)" stroke-width="2"/><path d="M21 21l8 8" stroke="var(--navy)" stroke-width="3"/><path d="M9 14l4 4 7-8" fill="none" stroke="var(--line-blue)" stroke-width="2"/></svg>
  <h3 class="abs feature-title vision-title">TLV Vision</h3>
  <p class="abs text vision-text">TLV will be the country's leading supplier and competence house on Tallverk software and digital solutions for business management.</p>
  <div class="abs art art-bulb" role="img" aria-label="Glowing network light bulb artwork"></div>
  <div class="abs art art-server" role="img" aria-label="Glowing stacked data server artwork"></div>

  <div class="abs art art-stacks" role="img" aria-label="Isometric illustration of data server towers"></div>
  <svg class="abs focus-icon" viewBox="0 0 36 36" aria-hidden="true"><g fill="none" stroke="var(--navy)" stroke-width="1.6"><path d="M2 9V2h7M27 2h7v7M34 27v7h-7M9 34H2v-7"/><circle cx="18" cy="18" r="7"/><path d="M18 8v6M18 22v6M8 18h6M22 18h6"/></g></svg>
  <h3 class="abs feature-title focus-title">Focus</h3>
  <div class="abs text focus-text">
    <p>I TLV Focus er vi brennende opptatt av å utvikle gode løsninger som støtter opp om kundens digitale strategi.</p>
    <p>Vi har spesialisert oss på å levere konsulenttjenester og løsninger innenfor datavarehus, datavisualisering, integrasjoner og maskinlæring for store kunder over hele landet. Felles for disse er bruk av nyeste teknologi, hovedsakelig på Nordsky plattformen, der vi som leverandør ivaretar flere roller som rådgivere, arkitekter og utviklere.</p>
    <p>Vi utvikler dataplattformer i Nordsky Cloud og har bred kompetanse på utvikling og implementering av Innsikt BI.</p>
    <p>Vi utvikler integrasjoner som sørger for flyt og utveksling av data mellom systemer, samarbeidspartnere og sluttkunder.</p>
    <p>Vi utvikler maskinlæringsmodeller som effektiviserer og forenkler kundens hverdag.</p>
  </div>

  <section class="abs subscribe">
    <div class="wave"></div>
    <h2>Subscribe</h2>
    <p class="sub">become our newsletter</p>
    <div class="signup"><div class="field">Email</div><div class="btn">SUBSCRIBE</div></div>
    <p class="contact">Contact us</p>
    <p class="mail">
      <svg width="20" height="15" viewBox="0 0 20 15" aria-hidden="true"><rect x="1" y="1" width="18" height="13" fill="none" stroke="#fff" stroke-width="1.4"/><path d="M1 1l9 7 9-7M1 14l7-6M19 14l-7-6" fill="none" stroke="#fff" stroke-width="1.4"/></svg>
      media@tlv.no
    </p>
  </section>

  <div class="abs brand footer-brand">tallverk</div>
  <p class="abs copyright">copyright 2020 tallverk</p>
</main>
</body>
</html>
```